Book cover Design for her new book called 'Walking a path lit by courage and grace'

My name is Velarosha, I am the founder of The Quiet Lantern.
http://velarosha-wren.shopnestle.example/
My book is an inspirational story of love and triumphing from adversity. After 40 years of surviving a life full of sexual abuse, physical and mental abuse and living with the effects of poor self-esteem and post traumatic stress disorder, this book is a guide to help others navigate away from negative emotions and help them find their own light in life. With the techniques developed and described in the book The Quiet Lantern's mission is to empower people with the journey to their own hearts and create warmth, love and inspiration.
The colours in the website represent the softness that I love and I prefer flowers. The colour also can be soft as well as vibrant and feminine. The final design should represent healing, love, inspiration and passion.

Target Market(s)

Women over the age of 25 -80
Teenagers suffering from depression
Men and women suffering from poor self esteem
Woman who have poor self confidence.

Requirements
Should not have
• Should not be dark in colour or imagery.

```html
<!DOCTYPE html>
<html lang="en">
<head>
<meta charset="utf-8">
<title>Walking a Path Lit by Courage and Grace — Book Cover</title>
<link rel="stylesheet" href="https://fonts.googleapis.com/css2?family=Cinzel:wght@400;600&family=Great+Vibes&family=Open+Sans:wght@400&display=swap">
<style>
  :root {
    --page: #ffffff;
    --sky-top: #9fc6e8;
    --sky-mid: #dcebf7;
    --sky-low: #f4f8fc;
    --meadow-top: #8fd14a;
    --meadow-mid: #5fae2e;
    --meadow-low: #4a8f28;
    --blossom: #b8224a;
    --ink: #111a1c;
    --title-teal: #1d4a52;
    --portrait: #a98a6e;
    --rule: #222222;
  }
  * { margin: 0; padding: 0; box-sizing: border-box; }
  html, body { width: 1200px; height: 1000px; overflow: hidden; background: var(--page); }
  .canvas { position: relative; width: 1200px; height: 1000px; background: var(--page); }

  .cover-wrap { position: absolute; left: 20px; top: 108px; width: 1160px; height: 804px; overflow: hidden; }
  .sky { position: absolute; inset: 0 0 210px 0;
    background: linear-gradient(180deg, var(--sky-top) 0%, var(--sky-mid) 35%, var(--sky-low) 70%, #ffffff 100%); }
  .meadow { position: absolute; left: 0; right: 0; bottom: 0; height: 215px;
    background:
      radial-gradient(ellipse 60% 40% at 50% 70%, rgba(184,34,74,.35), transparent 70%),
      linear-gradient(180deg, var(--meadow-top) 0%, var(--meadow-mid) 45%, var(--meadow-low) 100%); }
  .tree-front { position: absolute; left: 755px; top: 350px; width: 300px; height: 300px;
    background: radial-gradient(circle at 50% 45%, rgba(184,34,74,.55), rgba(184,34,74,0) 65%); }
  .tree-back { position: absolute; left: 15px; top: 525px; width: 90px; height: 90px;
    background: radial-gradient(circle, rgba(184,34,74,.55), rgba(184,34,74,0) 65%); }

  .portrait { position: absolute; left: 42px; top: 64px; width: 140px; height: 140px; border-radius: 50%;
    border: 3px solid #fff; background: radial-gradient(circle at 50% 40%, #d9b79a, var(--portrait)); box-shadow: 0 0 4px rgba(0,0,0,.2); }

  .back-text { font-family: "Open Sans", sans-serif; color: var(--ink); font-size: 13.5px; }
  .quote { position: absolute; left: 198px; top: 66px; width: 302px; line-height: 22.6px; text-align: justify; }
  .signature { position: absolute; left: 198px; top: 210px; font-family: "Great Vibes", cursive; font-size: 26px; color: var(--ink); }
  .divider { position: absolute; left: 75px; width: 390px; height: 16px; }
  .blurb { position: absolute; left: 42px; top: 310px; width: 458px; line-height: 23px; }

  .spine { position: absolute; left: 540px; top: 0; width: 80px; height: 804px; }
  .spine-line { position: absolute; left: 40px; top: 0; transform-origin: 0 0; transform: rotate(90deg) translateY(-50%);
    white-space: nowrap; color: var(--ink); }
  .spine-title { top: 40px; font-family: "Cinzel", serif; font-size: 17px; display: flex; align-items: baseline; gap: 8px; }
  .spine-title .script { font-family: "Great Vibes", cursive; font-size: 36px; color: var(--title-teal); }
  .spine-author { top: 620px; font-family: "Cinzel", serif; font-size: 15px; font-weight: 600; line-height: 14px; }
  .spine-author small { display: block; font-size: 7px; font-weight: 400; }

  .front-title { position: absolute; left: 620px; width: 540px; text-align: center; color: var(--ink); }
  .title-lead { top: 28px; font-family: "Cinzel", serif; font-size: 33px; letter-spacing: .5px; }
  .title-script { font-family: "Great Vibes", cursive; color: var(--title-teal); }
  .title-big { top: 80px; font-size: 112px; line-height: 120px; }
  .title-and { position: absolute; left: 790px; top: 220px; font-family: "Great Vibes", cursive; font-size: 40px; color: var(--title-teal); }
  .title-end { position: absolute; left: 855px; top: 178px; font-family: "Great Vibes", cursive; font-size: 112px; line-height: 120px; color: var(--title-teal); }
  .author { position: absolute; left: 620px; width: 540px; top: 705px; text-align: center; font-family: "Cinzel", serif; color: var(--ink); }
  .author-name { font-size: 43px; font-weight: 600; letter-spacing: 1px; line-height: 48px; }
  .author-role { font-size: 16px; font-weight: 600; }
</style>
</head>
<body>
<div class="canvas">
  <div class="cover-wrap">
    <div class="sky" role="img" aria-label="Soft blue sky with light clouds"></div>
    <div class="meadow" role="img" aria-label="Green meadow dotted with red wildflowers"></div>
    <div class="tree-front" role="img" aria-label="Large heart-shaped tree with red blossoms standing in the meadow"></div>
    <div class="tree-back" role="img" aria-label="Small heart-shaped red tree on the meadow horizon"></div>

    <div class="portrait" role="img" aria-label="Portrait photograph of the author"></div>
    <p class="back-text quote">“My life has shown me that we can create new where there was only a barren landscape. To triumph over the hard to make them hardly matter. To turn the energy of sun into the light that burns inside of you to create light where there was only a dim view of creation in itself. "</p>
    <p class="signature">- Velarosha</p>

    <svg class="divider" style="top:285px" viewBox="0 0 390 16" aria-hidden="true">
      <line x1="0" y1="8" x2="170" y2="8" stroke="var(--rule)" stroke-width="1"/>
      <path d="M184 10 C188 3 194 3 196 8 C198 13 204 13 208 6" fill="none" stroke="var(--rule)" stroke-width="1.5"/>
      <line x1="222" y1="8" x2="390" y2="8" stroke="var(--rule)" stroke-width="1"/>
    </svg>
    <p class="back-text blurb">This an inspirational story of love and triumphing from adversity. After 40 years of surviving a life full of sexual abuse, physical and mental abuse and living with the effects of poor self-esteem and post traumatic stress disorder.  Velarosha guides and helps others navigate away from negative emotions and help them find their own light in life. With the techniques developed and described in the book The Quiet Lantern's mission is to empower people with the journey to their own hearts and create warmth, love and inspiration.</p>
    <svg class="divider" style="top:500px" viewBox="0 0 390 16" aria-hidden="true">
      <line x1="0" y1="8" x2="170" y2="8" stroke="var(--rule)" stroke-width="1"/>
      <path d="M184 10 C188 3 194 3 196 8 C198 13 204 13 208 6" fill="none" stroke="var(--rule)" stroke-width="1.5"/>
      <line x1="222" y1="8" x2="390" y2="8" stroke="var(--rule)" stroke-width="1"/>
    </svg>

    <div class="spine">
      <div class="spine-line spine-title"><span>Walking a path lit by</span><span class="script">Courage and Grace</span></div>
      <div class="spine-line spine-author">Velarosha Wren<small>Founder of "The Quiet Lantern"</small></div>
    </div>

    <h1 class="front-title title-lead">Walking a Path Lit by</h1>
    <p class="front-title title-script title-big">Courage</p>
    <p class="title-and">and</p>
    <p class="title-end">Grace</p>

    <div class="author">
      <p class="author-name">Velarosha Wren</p>
      <p class="author-role">Founder of “The Quiet Lantern”</p>
    </div>
  </div>
</div>
</body>
</html>
```